Zielgruppe
Wir sind ein Landwirtschaftsbetrieb für Obstbau und unsere Kunden sind hauptsächlich Privatpersonen und Familien aus der Region sowie Kleinbetriebe wie z. B. regionale Shops.
Aufgabenstellung
Wir benötigen Flaschenetiketten für Fruchtsäfte (3 verschiedene Sorten: Marillennektar, Pfirsichnektar, Kirschennektar) für 0,75 und 0,25 Liter Flaschen und für Schnaps und Liköre (Marillen, Kirschen, Pfirsich, Zwetschke, Kriecherl).
Wir würden eine Vorderseite, die das Design und die Pflichtangaben enthält, bevorzugen.
Die Schrift der Pflichtangaben muss wie folgt ausgeführt werden: Etiketten bis 80 cm2 Kleinbuchstaben mind. 0,9 mm, ab 80 cm2 Kleinbuchstaben mind. 1,2 mm, Großbuchstaben immer mind. 2 mm, das Feld benötigt in etwa 3,5 x 7 cm Platz. Für das Design gibt es noch keine fixe Größe.
Bitte keine Fotos von 'echtem' Obst verwenden.

```html
<!DOCTYPE html>
<html lang="de">
<head>
<meta charset="utf-8">
<title>Etiketten Marillen-Nektar und Marillen-Brand</title>
<link href="https://fonts.googleapis.com/css2?family=Archivo:wght@800&family=Fira+Sans+Extra+Condensed:wght@300;400;600&family=Mr+Dafoe&display=swap" rel="stylesheet">
<style>
  :root {
    --page: #f4f3f0;
    --paper: #ffffff;
    --sketch-light: #ececec;
    --sketch-mid: #cfcfcf;
    --nectar-yellow: #f2c200;
    --apricot-gold: #e9b400;
    --apricot-light: #f5c93a;
    --title-red: #e2412b;
    --ink: #1a1a1a;
    --ink-soft: #3a3a2a;
    --band-grey: #b9b9b9;
    --foil-gold: #e0b11a;
    --foil-deep: #b88a05;
  }
  * { box-sizing: border-box; margin: 0; padding: 0; }
  html, body { width: 907px; height: 1200px; overflow: hidden; }
  body {
    background: var(--page);
    font-family: "Fira Sans Extra Condensed", "Arial Narrow", sans-serif;
    color: var(--ink);
    position: relative;
  }

  /* ---------- shared label parts ---------- */
  .label { position: absolute; background: var(--paper); overflow: hidden; box-shadow: 0 2px 10px rgba(0,0,0,.08); }
  .orchard-scene {
    position: absolute; left: 0; top: 0; width: 100%;
    background: linear-gradient(180deg, var(--sketch-light) 0%, #f6f6f6 55%, var(--sketch-mid) 100%);
  }
  .brand-mark {
    position: absolute; left: 50%; transform: translateX(-50%);
    display: flex; align-items: center; gap: 5px;
    background: var(--paper); border-radius: 14px;
    font-weight: 600; letter-spacing: .04em; color: var(--ink);
    white-space: nowrap;
  }
  .brand-mark .dot { border-radius: 50%; background: var(--title-red); flex: none; }
  .script { font-family: "Mr Dafoe", cursive; font-weight: 400; color: var(--ink); }
  .caps-title { font-family: "Archivo", "Arial Black", sans-serif; font-weight: 800; letter-spacing: .06em; }

  /* ---------- nectar label ---------- */
  .label--nectar { left: 48px; top: 318px; width: 420px; height: 578px; }
  .label--nectar .orchard-scene { height: 384px; }
  .label--nectar .brand-mark { top: 36px; padding: 5px 10px; font-size: 12px; }
  .label--nectar .brand-mark .dot { width: 12px; height: 12px; }
  .nectar-apricot {
    position: absolute; left: 66px; top: 104px; width: 300px; height: 300px;
  }
  .nectar-title { position: absolute; left: 0; width: 100%; text-align: center; }
  .nectar-title .caps-title { position: absolute; left: 0; right: 0; top: 216px; font-size: 42px; color: var(--title-red); }
  .nectar-title .script { position: absolute; left: 132px; top: 252px; font-size: 64px; line-height: 1; }

  .nectar-info {
    position: absolute; left: 0; top: 384px; width: 100%; height: 194px;
    background: var(--nectar-yellow);
    display: grid; grid-template-columns: 1fr 1fr; column-gap: 14px;
    padding: 14px 14px 10px 14px;
    font-size: 13px; line-height: 1.5; color: var(--ink-soft); font-weight: 300;
  }
  .nectar-info strong { font-weight: 600; color: var(--ink); }
  .nectar-info .producer { margin-top: 6px; }
  .nectar-info .volume { margin-top: 10px; font-size: 24px; font-weight: 600; color: var(--ink); }

  /* ---------- spirit label ---------- */
  .label--spirit { left: 560px; top: 408px; width: 268px; height: 430px; }
  .label--spirit .orchard-scene { height: 300px; }
  .label--spirit .brand-mark { top: 22px; padding: 3px 8px; font-size: 9px; }
  .label--spirit .brand-mark .dot { width: 9px; height: 9px; }
  .spirit-apricot { position: absolute; left: 78px; top: 236px; width: 112px; height: 64px; }
  .spirit-band {
    position: absolute; left: 0; top: 300px; width: 100%; height: 130px;
    background: var(--band-grey);
  }
  .spirit-band .caps-title {
    position: absolute; left: 0; right: 0; top: 12px; text-align: center;
    font-size: 34px; color: var(--foil-gold);
  }
  .spirit-band .script { position: absolute; left: 78px; top: 36px; font-size: 50px; line-height: 1; }
  .spirit-band .spec { position: absolute; bottom: 20px; font-size: 12px; font-weight: 300; color: var(--ink-soft); }
  .spirit-band .spec--abv { left: 12px; }
  .spirit-band .spec--size { right: 12px; }
</style>
</head>
<body>

  <section class="label label--nectar" aria-label="Etikett Marillen-Nektar">
    <div class="orchard-scene" role="img" aria-label="Strichzeichnung: Obstgarten mit Erntehelfern, Leiter und Körben"></div>
    <div class="brand-mark"><span class="dot"></span>OBSTBAU-BERGHOFER</div>
    <svg class="nectar-apricot" viewBox="0 0 300 300" role="img" aria-label="stilisierte Marille">
      <defs>
        <linearGradient id="apricotFill" x1="0" y1="0" x2="1" y2="1">
          <stop offset="0" stop-color="#f7cf4a"/>
          <stop offset="1" stop-color="#e8b000"/>
        </linearGradient>
      </defs>
      <circle cx="150" cy="160" r="150" fill="url(#apricotFill)"/>
    </svg>
    <h1 class="nectar-title">
      <span class="caps-title">MARILLEN</span>
      <span class="script">Nektar</span>
    </h1>
    <div class="nectar-info">
      <div class="facts">
        <strong>Marillen-Nektar</strong><br>
        <strong>Fruchtgehalt: mindestens 50%</strong><br>
        <strong>Zutaten:</strong> Wasser, Fruchtfleisch, Zucker, Säuerungsmittel: Zitronensäure, Antioxidationsmittel: Ascorbinsäure<br>
        Vor Gebrauch gut schütteln.
        <p class="producer">Anton Berghofer - Kirchgasse 14<br>2282 Wiesenfeld</p>
      </div>
      <div class="handling">
        Vor Gebrauch gut schütteln.<br>
        Innerhalb von 3 Tagen verbrauchen.<br>
        Kühl und dunkel lagern.<br>
        Ungeöffnet mindestens haltbar bis: siehe Verschluss.
        <p class="volume">0,75 L</p>
      </div>
    </div>
  </section>

  <section class="label label--spirit" aria-label="Etikett Marillen-Brand">
    <div class="orchard-scene" role="img" aria-label="Strichzeichnung: Obstgarten mit Erntehelfern und Leiter"></div>
    <div class="brand-mark"><span class="dot"></span>OBSTBAU-BERGHOFER</div>
    <svg class="spirit-apricot" viewBox="0 0 112 64" role="img" aria-label="stilisierte Marille in Goldfolie">
      <defs>
        <linearGradient id="foilFill" x1="0" y1="0" x2="1" y2="0">
          <stop offset="0" stop-color="#b88a05"/>
          <stop offset=".45" stop-color="#f2cf3a"/>
          <stop offset="1" stop-color="#c99806"/>
        </linearGradient>
      </defs>
      <path d="M2 64 A54 54 0 0 1 110 64 Z" fill="url(#foilFill)"/>
    </svg>
    <div class="spirit-band">
      <h2 class="caps-title">MARILLEN</h2>
      <span class="script">Brand</span>
      <span class="spec spec--abv">40% Vol.</span>
      <span class="spec spec--size">500 ml</span>
    </div>
  </section>

</body>
</html>
```